Ironvale Holdings Business card

We need a an amazing matte black and gold card! W are a finance investing company so we want something that's eye catching and sleek. We want it to be attractive and sleek and represent money. Heck with would like the letters and lgo to be printed as 24k gold one day. We have the logo added so please use the color scheme with the logo and have that beautifully placed on one side.

Target Market(s)

Investors of all ages

Industry/Entity Type

Financial

Contact Information for Business Card

Black and matte with gold lettering follow logo colrs please.

Font styles to use
Other font styles liked:
• you decide

Colors

Designer to choose colors to be used in the design.

Requirements
Must have
• Matte Black and Gold, logo on one side. job title and name , website, phone number and email address on the other side
Nice to have
• Matte black and crisp finish to attract investors
Should not have
• playful, very professional!

```html
<!DOCTYPE html>
<html lang="en">
<head>
<meta charset="utf-8">
<title>Ironvale Holdings — Business Card</title>
<link rel="stylesheet" href="https://fonts.googleapis.com/css2?family=Quicksand:wght@500;600;700&display=swap">
<style>
  :root {
    --backdrop: #e9e7e3;
    --card-black: #050505;
    --pattern-brown: #2b201b;
    --pattern-glow: #3a2a1e;
    --gold-light: #f3cf6a;
    --gold: #d4a437;
    --gold-deep: #9c6e1c;
  }
  * { margin: 0; padding: 0; box-sizing: border-box; }
  html, body {
    width: 1200px;
    height: 892px;
    overflow: hidden;
    background: var(--backdrop);
  }
  .canvas {
    width: 1200px;
    height: 892px;
    display: flex;
    align-items: center;
    justify-content: center;
    gap: 50px;
  }
  .card {
    position: relative;
    width: 540px;
    height: 309px;
    background: var(--card-black);
    overflow: hidden;
    box-shadow: 0 8px 24px rgba(0,0,0,0.25);
  }
  .card-art {
    position: absolute;
    inset: 0;
    width: 100%;
    height: 100%;
  }
  .brand-name {
    position: absolute;
    left: 200px;
    top: 124px;
    width: 290px;
    text-align: center;
    font-family: "Quicksand", sans-serif;
    font-weight: 600;
    color: var(--gold);
    line-height: 1;
  }
  .brand-name .brand-primary {
    display: block;
    font-size: 36px;
    letter-spacing: 3px;
  }
  .brand-name .brand-secondary {
    display: block;
    margin-top: 8px;
    font-size: 17px;
    letter-spacing: 7px;
  }
  .contact-block {
    position: absolute;
    left: 0;
    right: 0;
    top: 84px;
    text-align: center;
    font-family: "Quicksand", sans-serif;
    font-style: normal;
    font-weight: 600;
    font-size: 13.5px;
    line-height: 1.45;
    color: var(--gold);
  }
  .contact-block .person-name {
    font-weight: 700;
    font-size: 17px;
    letter-spacing: 1px;
  }
  .contact-block .job-title {
    font-size: 12px;
    letter-spacing: 2px;
    text-transform: uppercase;
    margin-bottom: 12px;
  }
  .contact-block .address { margin-bottom: 12px; }
</style>
</head>
<body>
<main class="canvas">

  <section class="card card-front" aria-label="Card front">
    <svg class="card-art" viewBox="0 0 540 309">
      <defs>
        <linearGradient id="goldFoil" x1="0" y1="1" x2="1" y2="0">
          <stop offset="0" stop-color="#9c6e1c"/>
          <stop offset="0.5" stop-color="#f3cf6a"/>
          <stop offset="1" stop-color="#9c6e1c"/>
        </linearGradient>
        <radialGradient id="patternTone" cx="0.4" cy="0.4" r="0.8">
          <stop offset="0" stop-color="#3a2a1e"/>
          <stop offset="1" stop-color="#2b201b"/>
        </radialGradient>
      </defs>
      <polygon class="pattern-panel" role="img" aria-label="Gold dot pattern on dark brown"
               points="0,0 320,0 55,309 0,309" fill="url(#patternTone)"/>
      <polygon class="pattern-panel" role="img" aria-label="Gold dot pattern on dark brown"
               points="405,309 540,175 540,309" fill="url(#patternTone)"/>
      <line class="gold-rule" x1="320" y1="0" x2="55" y2="309" stroke="url(#goldFoil)" stroke-width="3"/>
      <line class="gold-rule" x1="405" y1="309" x2="540" y2="175" stroke="url(#goldFoil)" stroke-width="3"/>
    </svg>
    <h1 class="brand-name">
      <span class="brand-primary">IRONVALE</span>
      <span class="brand-secondary">HOLDINGS</span>
    </h1>
  </section>

  <section class="card card-back" aria-label="Card back">
    <svg class="card-art" viewBox="0 0 540 309" aria-hidden="true">
      <defs>
        <linearGradient id="goldFoilBack" x1="0" y1="0" x2="1" y2="0">
          <stop offset="0" stop-color="#9c6e1c"/>
          <stop offset="0.55" stop-color="#f3cf6a"/>
          <stop offset="1" stop-color="#9c6e1c"/>
        </linearGradient>
      </defs>
      <line class="gold-rule" x1="0" y1="118" x2="210" y2="0" stroke="url(#goldFoilBack)" stroke-width="3"/>
      <line class="gold-rule" x1="330" y1="309" x2="540" y2="191" stroke="url(#goldFoilBack)" stroke-width="3"/>
    </svg>
    <address class="contact-block">
      <p class="person-name">Daniel Marsh</p>
      <p class="job-title">Investment Director</p>
      <p class="address">24 The Street, Your Town<br>Your City, Zip Code</p>
      <p class="phone">Tel: 0000 000000</p>
      <p class="web">www.ironvaleholdings.com</p>
      <p class="email">info@ironvaleholdings.com</p>
    </address>
  </section>

</main>
</body>
</html>
```